Brenwick Realty
Business cards and stationery
Brenwick Realty - Real Estate
Creative Brief
Modern
Marian Talcott
Director
Level 4 218 Garnet Lane Melbourne VIC 3000
marian@brenwickrealty-example.com.au
www.brenwickrealty-example.com.au
Brenwick Summit Realty 518902K Licensee Marian Talcott
Stationery needs to have the licensee info on the bottom of letterhead
black background logo in centre

```html
<!DOCTYPE html>
<html lang="en">
<head>
<meta charset="utf-8">
<title>Brenwick Realty – Business Card</title>
<link href="https://fonts.googleapis.com/css2?family=Open+Sans:wght@400;700;800&display=swap" rel="stylesheet">
<style>
  :root {
    --page: #ecebe8;
    --card-black: #0d0d0f;
    --magenta: #b0125f;
    --magenta-deep: #7d0b43;
    --blue: #29a6dd;
    --pink: #e2419a;
    --white: #ffffff;
  }
  html, body {
    margin: 0;
    width: 1200px;
    height: 780px;
    overflow: hidden;
    background: var(--page);
    font-family: "Open Sans", Arial, sans-serif;
  }
  .card {
    position: absolute;
    left: 80px;
    top: 80px;
    width: 1040px;
    height: 620px;
    border-radius: 28px;
    overflow: hidden;
    background: var(--card-black);
    box-shadow: 0 10px 30px rgba(0,0,0,0.18);
  }
  .card-shapes { position: absolute; inset: 0; }
  .brand {
    position: absolute;
    left: 70px;
    top: 245px;
    display: flex;
    align-items: center;
    gap: 16px;
  }
  .brand-dot {
    width: 26px; height: 26px;
    border-radius: 50%;
    background: var(--blue);
  }
  .brand-name {
    color: var(--pink);
    font-weight: 800;
    font-size: 54px;
    letter-spacing: -1px;
    line-height: 1;
  }
  .person {
    position: absolute;
    right: 70px;
    top: 40px;
    text-align: right;
    color: var(--white);
  }
  .person-name { font-weight: 700; font-size: 30px; margin: 0; }
  .person-role { font-size: 18px; margin: 4px 0 0; }
  .address {
    position: absolute;
    right: 70px;
    top: 300px;
    text-align: right;
    color: var(--white);
    font-size: 20px;
    line-height: 1.35;
    font-style: normal;
  }
  .contact {
    position: absolute;
    color: var(--white);
    font-size: 19px;
    display: flex;
    align-items: center;
    gap: 10px;
  }
  .contact svg { width: 20px; height: 20px; fill: var(--white); }
  .phone-office { left: 480px; top: 450px; }
  .phone-mobile { left: 790px; top: 435px; }
  .phone-fax { left: 790px; top: 469px; }
  .email { left: 480px; top: 530px; }
</style>
</head>
<body>
  <div class="card">
    <svg class="card-shapes" width="1040" height="620" viewBox="0 0 1040 620">
      <defs>
        <linearGradient id="magentaFill" x1="0" y1="0" x2="0" y2="1">
          <stop offset="0" stop-color="#b0125f"/>
          <stop offset="1" stop-color="#7d0b43"/>
        </linearGradient>
      </defs>
      <path d="M0,474 C420,454 720,374 1040,154 L1040,620 L0,620 Z" fill="url(#magentaFill)"/>
      <path d="M0,460 C420,440 720,360 1040,140" fill="none" stroke="#29a6dd" stroke-width="7"/>
    </svg>

    <div class="brand">
      <span class="brand-dot"></span>
      <span class="brand-name">Brenwick Realty</span>
    </div>

    <div class="person">
      <p class="person-name">Marian Talcott</p>
      <p class="person-role">Director</p>
    </div>

    <address class="address">
      Level 4<br>
      218 Garnet Lane<br>
      Melbourne VIC 3000
    </address>

    <div class="contact phone-office">
      <svg viewBox="0 0 24 24"><path d="M6.6 10.8a15 15 0 0 0 6.6 6.6l2.2-2.2c.3-.3.7-.4 1-.2 1.1.4 2.3.6 3.6.6.6 0 1 .4 1 1V20c0 .6-.4 1-1 1A17 17 0 0 1 3 4c0-.6.4-1 1-1h3.5c.6 0 1 .4 1 1 0 1.3.2 2.5.6 3.6.1.3 0 .7-.2 1z"/></svg>
      <span>03 9555 0142</span>
    </div>
    <div class="contact phone-mobile">
      <svg viewBox="0 0 24 24"><path d="M7 2h10a1 1 0 0 1 1 1v18a1 1 0 0 1-1 1H7a1 1 0 0 1-1-1V3a1 1 0 0 1 1-1zm1 3v12h8V5zm4 13.5a1 1 0 1 0 0 2 1 1 0 0 0 0-2z"/></svg>
      <span>0491 570 156</span>
    </div>
    <div class="contact phone-fax">
      <svg viewBox="0 0 24 24"><path d="M7 3h8l2 2v4H7zM4 10h16a1 1 0 0 1 1 1v7a1 1 0 0 1-1 1h-3v2H7v-2H4a1 1 0 0 1-1-1v-7a1 1 0 0 1 1-1zm4 6v3h8v-3z"/></svg>
      <span>03 9555 0187</span>
    </div>
    <div class="contact email">
      <svg viewBox="0 0 24 24"><path d="M3 5h18a1 1 0 0 1 1 1v12a1 1 0 0 1-1 1H3a1 1 0 0 1-1-1V6a1 1 0 0 1 1-1zm1 2.5V17h16V7.5l-8 5z"/></svg>
      <span>marian@brenwickrealty-example.com.au</span>
    </div>
  </div>
</body>
</html>
```